Verpackungen für Klangschalenuhren
Zielgruppe
Unter der Marke 'Velmora' werden manufakturartig Klangschalenuhren in geringen Stückzahlen hergestellt. Produktionsort ist Deutschland, bis auf die Klangschalen.
Bei Klangschalenuhren wird mechanisch eine Klangschale angeschlagen.
Vorteile / Einsatz: Sanftes Aufwachen mit einer Klangschale / Ambiente: Hauch von Asien im Wohnbereich / Meditation & Wellness / Sitzungen, Behandlungen und Meetings
Zielgruppe:
„LOHAS“: kaufkräftig, bewusstes Leben, gesundheitsorientiert, natürliche/nachhaltige Produkte, Fairtrade/ethisches Handeln, authentisch. Selbständige (z.B. Therapeuten). Wellness.
Aufgabenstellung
Die Produktverpackung steht nicht im Verkaufsregal und muss daher kaum informative Elemente über das Produkt enthalten. Der Kunde sieht Verpackung beim Auspacken aus Versandkarton oder im Onlineshop.
WERTIG, NATÜRLICH, SCHLICHT. Kunde soll bei Empfang und Auspacken seines Produkts Freude empfinden.
Es gibt nur eine Verpackung für viele Modelle / Produktvarianten -> Produktfotos nicht geeignet.
Designelemente (Minimum):
Logo mit Claim „Der Klang der Zeit“. Mindestens auf Frontseite und Klappdeckel.
Ergänzen um ein stilisiertes Bild mit einer (angeschnittenen) Klangschale mit Klöppel
Handwerk aus Deutschland (mit oder ohne Symbol)
Adressdaten:
Velmora
Lindenstieg 9
64712 Tannbrück-Eschenau
Deutschland
www.velmora-beispiel.de
Feld für Artikelaufkleber: 5 x 3 cm (bxh)
Zu bedruckender Karton:
Steckbodenschachtel
Größe 245 x 245 x 205 mm
aus Mikrowellpappe E-Welle innen braun
kaschiert mit GD2-Karton 230 g/qm
4/0-farbig bedruckt u. Dispersionsglanzlack

```html
<!DOCTYPE html>
<html lang="de">
<head>
<meta charset="utf-8">
<title>Velmora – Verpackung Klangschalenuhr</title>
<link href="https://fonts.googleapis.com/css2?family=Questrial&family=Raleway:wght@200;300&display=swap" rel="stylesheet">
<style>
  :root {
    --page: #ffffff;
    --board: #f7ecd9;
    --board-warm: #f0dfbf;
    --ink: #333333;
    --text: #3a3530;
    --cut: #2aa84a;
    --fold: #6e6a66;
    --gold: #e3c79a;
    --url: #e6d0a8;
    --label: #fbf5ea;
  }
  * { margin: 0; padding: 0; box-sizing: border-box; }
  html, body { width: 1200px; height: 903px; overflow: hidden; background: var(--page); }
  .canvas { position: relative; width: 1200px; height: 903px; font-family: "Questrial", sans-serif; color: var(--text); }
  .dieline { position: absolute; left: 0; top: 0; }
  .abs { position: absolute; }
  .brand-mark { left: 76px; top: 50px; font-family: "Questrial", sans-serif; font-size: 66px; line-height: 1; color: var(--ink); letter-spacing: 1px; }
  .wordmark { font-family: "Questrial", sans-serif; color: var(--ink); text-align: center; white-space: nowrap; line-height: 1; }
  .claim { font-family: "Raleway", sans-serif; font-weight: 300; color: var(--ink); white-space: nowrap; line-height: 1; }
  .product-line { font-family: "Raleway", sans-serif; font-weight: 300; color: var(--ink); white-space: nowrap; line-height: 1; }
  .bowl-art { background: linear-gradient(180deg, rgba(227,199,154,0.15), rgba(227,199,154,0.55)); border-radius: 0 0 40px 40px; }
  .copy { font-size: 5.6px; line-height: 11.3px; text-align: center; color: var(--text); white-space: nowrap; }
  .copy p + p { margin-top: 6px; }
  .address { font-size: 6.6px; line-height: 8px; color: var(--ink); white-space: nowrap; }
  .url { font-size: 14px; line-height: 1; color: var(--url); white-space: nowrap; }
  .label-field { background: var(--label); }
</style>
</head>
<body>
<div class="canvas">
  <div class="abs brand-mark">Velmora</div>

  <svg class="dieline" width="1200" height="903" viewBox="0 0 1200 903">
    <defs>
      <linearGradient id="panelShade" x1="0" x2="1" y1="0" y2="0">
        <stop offset="0" stop-color="#f0dfbf"/>
        <stop offset="0.35" stop-color="#f7ecd9"/>
        <stop offset="0.7" stop-color="#f7ecd9"/>
        <stop offset="1" stop-color="#f0dfbf"/>
      </linearGradient>
    </defs>
    <polygon points="65,189 373,189 373,411 1153,411 1153,877 65,877" fill="var(--board)"/>
    <rect x="97" y="219" width="259" height="261" fill="url(#panelShade)"/>
    <rect x="97" y="480" width="1033" height="216" fill="url(#panelShade)"/>
    <g fill="none" stroke="var(--cut)" stroke-width="0.8">
      <path d="M97,219 L97,213 Q97,195 115,195 L337,195 Q355,195 355,213 L355,219"/>
      <line x1="97" y1="219" x2="97" y2="480"/>
      <line x1="356" y1="219" x2="356" y2="480"/>
      <polyline points="97,482 76,487 76,689 97,694"/>
      <polyline points="356,480 356,429 598,429 610,470 613,480"/>
      <polyline points="1130,480 1130,429 887,429 875,470 872,480"/>
      <path d="M712,500 L712,468 Q712,460 720,460 L766,460 Q774,460 774,468 L774,500"/>
      <path d="M732,481 A11,11 0 0 0 754,481"/>
      <line x1="613" y1="480" x2="872" y2="480"/>
      <path d="M97,696 L161,822 L161,832 Q161,843 172,843 L280,843 Q291,843 291,832 L291,822 L356,696"/>
      <polyline points="356,696 356,819 484,819 484,759 613,696"/>
      <polyline points="613,696 613,843 677,843 677,822 808,822 808,843 872,843 872,696"/>
      <polyline points="872,696 1002,759 1002,819 1130,819 1130,696"/>
      <line x1="1130" y1="480" x2="1130" y2="696"/>
    </g>
    <g stroke="var(--fold)" stroke-width="0.7">
      <line x1="110" y1="220" x2="343" y2="220"/>
      <line x1="97" y1="480" x2="613" y2="480"/>
      <line x1="872" y1="480" x2="1130" y2="480"/>
      <line x1="97" y1="696" x2="1130" y2="696"/>
      <line x1="356" y1="480" x2="356" y2="696"/>
      <line x1="613" y1="480" x2="613" y2="696"/>
      <line x1="872" y1="480" x2="872" y2="696"/>
    </g>
  </svg>

  <!-- Lid -->
  <div class="abs wordmark" style="left:97px; width:259px; top:302px; font-size:44px;">Velmora</div>
  <div class="abs claim" style="left:97px; width:259px; top:378px; font-size:20px; text-align:center;">Der Klang der Zeit</div>
  <div class="abs bowl-art" role="img" aria-label="Stilisierte Klangschale mit Klöppel" style="left:200px; top:414px; width:58px; height:44px;"></div>

  <!-- Front -->
  <div class="abs wordmark" style="left:97px; width:259px; top:546px; font-size:34px;">Velmora</div>
  <div class="abs bowl-art" role="img" aria-label="Stilisierte Klangschale mit Klöppel" style="left:200px; top:598px; width:58px; height:44px;"></div>
  <div class="abs product-line" style="left:97px; width:259px; top:650px; font-size:13px; text-align:center;">KLANGSCHALENUHR</div>

  <!-- Side: story -->
  <div class="abs copy" style="left:358px; width:254px; top:494px;">
    <p>Die perfekte Verbindung von Zeit und Klang</p>
    <p>Eines der letzten wirklichen Luxusgüter der Welt ist Zeit,<br>insbesondere die bewusst gelebte und erlebte Zeit.<br>Dabei geht es um weit mehr als um die Abfolge von Sekunden,<br>Minuten und Stunden in festgelegten Rhythmen von Arbeit und Freizeit.</p>
    <p>Für dieses sinnliche Zeiterlebnis verbinden wir Zeit und Klang<br>in unseren Velmora Klangschalenuhren.<br>Dazu verwenden wir die traditionellen Klangschalen aus Tibet, Nepal, Indien<br>und Japan, deren Klang eine spürbare Wirkung auf Körper, Geist und Seele hat.</p>
    <p>Für die Zeitmessung achten wir auf den Einsatz natürlicher Materialien<br>und eine nachhaltige Fertigung. Heimische Hölzer, ehrliche Handwerklichkeit<br>und der Klang fernöstlicher Klangschalen geben einer Velmora<br>ihren unnachahmlichen Charakter.</p>
    <p>Eine Velmora ist nicht nur ein Wecker – sie ist ein Lebensgefühl und<br>Ausdruck der Wertschätzung unserer Umwelt und unserer selbst.</p>
  </div>

  <!-- Back: address -->
  <div class="abs wordmark" style="left:638px; top:569px; font-size:20px; text-align:left;">Velmora</div>
  <div class="abs product-line" style="left:639px; top:601px; font-size:18px;">KLANGSCHALENUHR</div>
  <div class="abs address" style="left:639px; top:632px;">Velmora<br>Lindenstieg 9<br>64712 Tannbrück-Eschenau<br>Deutschland</div>
  <div class="abs url" style="left:638px; top:667px;">www.velmora-beispiel.de</div>
  <div class="abs label-field" style="left:804px; top:652px; width:53px; height:31px;"></div>

  <!-- Side: poem -->
  <div class="abs copy" style="left:874px; width:254px; top:597px;">
    Wir glauben seit Ewigkeiten, dass wir die Zeit nicht anhalten können.<br>
    Dass sie läuft in atemloser Schnelle.<br>
    Bis uns ein Klang berührt und ergreift.<br>
    Es ist der Ton einer Velmora, der uns inne halten lässt.<br>
    Er trägt uns fort mit leise wachsender Kraft.<br>
    Ins grenzenlose Ich und zurück.<br>
    Wir hören den Klang der Zeit und lächeln unendlich beglückt.<br>
    Denn wir sind ewig. Für diesen Moment.
  </div>
</div>
</body>
</html>
```